Heating - Cooling & Duct Cleaning Company

Our company name is Bramet we are a heating - cooling - duct cleaning company based in ottawa canada. we are looking for something very eye catching and out there! The wrap design must have the following details on it

Company Name - Bramet

Services We Provide - Heating - Cooling - Duct Cleaning

www.brametgroupe.net

555.418.2907

Industry/Entity Type

Hvac

Requirements
Must have
• Company Logo
• website
• number
• services heating - cooling - duct cleaning
• *note picture of truck attached in pictures
Nice to have
• something that stands out! very bold and flashy

```html
<!DOCTYPE html>
<html lang="en">
<head>
<meta charset="utf-8">
<title>Bramet – Box Truck Wrap</title>
<link rel="stylesheet" href="https://fonts.googleapis.com/css2?family=Exo+2:wght@300;400;700;800&family=Roboto+Condensed:wght@700&display=swap">
<style>
  :root {
    --bg: #ffffff;
    --panel: #f3f4f4;
    --blue: #1a9ad9;
    --red: #e3182d;
    --ink: #4a4a4a;
    --white: #ffffff;
    --furnace: #2b2b2b;
    --washer: #e4e6e8;
    --duct-a: #8a7460;
    --duct-b: #c8b9a6;
  }
  * { margin: 0; padding: 0; box-sizing: border-box; }
  html, body { width: 1200px; height: 849px; overflow: hidden; background: var(--bg); }
  .wrap-panel {
    position: absolute; left: 40px; top: 93px;
    width: 1120px; height: 662px;
    background: var(--panel); overflow: hidden;
    font-family: "Exo 2", sans-serif;
  }
  .wrap-panel svg.artwork { position: absolute; inset: 0; }
  .service-area {
    position: absolute; left: 71px; top: 100px;
    font-size: 33px; color: var(--ink); font-weight: 400; white-space: nowrap;
  }
  .service-area strong { font-weight: 700; }
  .brand-name {
    position: absolute; left: 790px; top: 68px;
    font-size: 86px; font-weight: 800; color: var(--red); letter-spacing: -1px;
  }
  .service {
    position: absolute; color: var(--blue); font-weight: 800;
    font-size: 31px; line-height: 31px; letter-spacing: 0.5px;
  }
  .service--heating { left: 143px; top: 256px; }
  .service--cooling { left: 388px; top: 256px; }
  .service--duct { left: 638px; top: 240px; }
  .contact-label {
    position: absolute; left: 71px; top: 398px;
    font-size: 37px; font-weight: 300; color: var(--ink);
  }
  .contact-phone {
    position: absolute; left: 71px; top: 436px;
    font-size: 52px; font-weight: 800; color: var(--red); letter-spacing: 2px;
  }
  .website {
    position: absolute; left: 635px; top: 590px;
    font-family: "Roboto Condensed", sans-serif;
    font-size: 44px; font-weight: 700; color: var(--white);
  }
</style>
</head>
<body>
<div class="wrap-panel">
  <svg class="artwork" viewBox="0 0 1120 662" width="1120" height="662">
    <!-- blue lower field -->
    <path d="M1120 110 C1060 230 920 360 760 440 C620 520 480 575 330 580 C180 585 60 560 0 470 L0 662 L1120 662 Z" fill="var(--blue)"/>
    <!-- white separator -->
    <path d="M1120 110 C1060 230 920 360 760 440 C620 520 480 575 330 580 C180 585 60 560 0 470" fill="none" stroke="var(--white)" stroke-width="8"/>
    <!-- red swoosh -->
    <path d="M1120 92 C1050 220 910 345 750 425 C610 500 470 555 330 562 C170 570 50 530 0 440" fill="none" stroke="var(--red)" stroke-width="12"/>

    <!-- service icons -->
    <g class="icon icon--heating" fill="none" stroke="var(--red)" stroke-width="2.5">
      <circle cx="101" cy="271" r="31" fill="var(--white)"/>
      <rect x="84" y="258" width="34" height="12" rx="2" fill="var(--blue)" stroke="none"/>
      <path d="M90 276 q3 4 0 8 M98 276 q3 4 0 8 M106 276 q3 4 0 8 M114 276 q3 4 0 8" stroke="var(--blue)" stroke-width="2"/>
    </g>
    <g class="icon icon--cooling">
      <circle cx="342" cy="271" r="31" fill="var(--white)" stroke="var(--red)" stroke-width="2.5"/>
      <circle cx="342" cy="268" r="15" fill="none" stroke="var(--blue)" stroke-width="3"/>
      <circle cx="342" cy="268" r="3" fill="var(--blue)"/>
      <path d="M342 268 l-6 -9 M342 268 l10 -2 M342 268 l-4 10" stroke="var(--blue)" stroke-width="4" stroke-linecap="round"/>
      <path d="M334 288 h16" stroke="var(--blue)" stroke-width="4"/>
    </g>
    <g class="icon icon--duct">
      <circle cx="589" cy="271" r="31" fill="var(--white)" stroke="var(--red)" stroke-width="2.5"/>
      <path d="M572 259 h34 l-4 10 h-26 Z" fill="var(--blue)"/>
      <path d="M578 263 h22" stroke="var(--white)" stroke-width="2"/>
      <path d="M581 274 v9 M589 274 v9 M597 274 v9" stroke="var(--blue)" stroke-width="2.5"/>
      <path d="M578 280 l3 4 l3 -4 M586 280 l3 4 l3 -4 M594 280 l3 4 l3 -4" fill="none" stroke="var(--blue)" stroke-width="2"/>
    </g>

    <!-- product photo circles -->
    <defs>
      <linearGradient id="duct-tones" x1="0" y1="0" x2="1" y2="1">
        <stop offset="0" stop-color="var(--duct-a)"/>
        <stop offset="1" stop-color="var(--duct-b)"/>
      </linearGradient>
    </defs>
    <ellipse cx="957" cy="478" rx="80" ry="6" fill="#0f6ea0" opacity="0.5"/>
    <circle cx="957" cy="354" r="115" fill="url(#duct-tones)" stroke="var(--red)" stroke-width="7" role="img" aria-label="Photo of dusty air ducts before cleaning"/>
    <ellipse cx="735" cy="555" rx="60" ry="5" fill="#0f6ea0" opacity="0.5"/>
    <circle cx="735" cy="455" r="94" fill="var(--washer)" stroke="var(--red)" stroke-width="7" role="img" aria-label="Photo of a white washer and dryer pair"/>
    <circle cx="544" cy="531" r="79" fill="var(--furnace)" stroke="var(--red)" stroke-width="7" role="img" aria-label="Photo of a high-efficiency gas furnace"/>

    <!-- social placeholders -->
    <circle cx="68" cy="614" r="18" fill="none" stroke="var(--white)" stroke-width="3"/>
    <circle cx="119" cy="614" r="18" fill="none" stroke="var(--white)" stroke-width="3"/>
  </svg>

  <p class="service-area">Serving <strong>Ottawa Brockville &amp;Kingston</strong></p>
  <p class="brand-name">Bramet</p>

  <p class="service service--heating">HEATING</p>
  <p class="service service--cooling">COOLING</p>
  <p class="service service--duct">DUCT<br>CLEANING</p>

  <p class="contact-label">CONTACT US TODAY</p>
  <p class="contact-phone">555.418.2907</p>

  <p class="website">www.BRAMETGROUPE.net</p>
</div>
</body>
</html>
```